Website design in Wordpress for Golf Simulator Center

We are opening a new golf simulator center in Copenhagen, and need a website design. We are using wordpress, and our site is https://fjordtee-play.dk
We will need a design for the frontpage, and a design for subpages (which we will be reusing for all subpages).
Logo is as seen on the site, and our base color scheme is leaf green.
As text, take the text on the current website, or put some placeholder text in english.
Should be responsive and look good on both desktop and mobile.
Target Market(s)
Male, 18-60, golf players
Coding
Coded - Design and coding required
Number of Pages Required
2 page
Font styles to use
Look and feel

```html
<!DOCTYPE html>
<html lang="da">
<head>
<meta charset="utf-8">
<title>Fjordtee Play – forside</title>
<link href="https://fonts.googleapis.com/css2?family=Oswald:wght@500;700&family=Montserrat:wght@400;600;700&display=swap" rel="stylesheet">
<style>
:root{
  --leaf:#1f8a1f;
  --leaf-bright:#2aa52a;
  --stage:#2e9a2e;
  --ink:#111;
  --dark:#0c0f0a;
  --dark-green:#1c2a17;
  --grey:#555;
  --paper:#fff;
  --teal:#17c08a;
}
*{margin:0;padding:0;box-sizing:border-box}
html,body{width:1200px;height:3086px;overflow:hidden;background:var(--paper);font-family:"Montserrat",sans-serif;color:var(--ink)}
.stage-band{position:absolute;left:0;top:0;width:1200px;height:525px;background:var(--stage)}
.board{position:absolute;overflow:hidden;background:var(--paper);box-shadow:0 4px 18px rgba(0,0,0,.12)}
.desktop{left:31px;top:591px;width:728px;height:2081px}
.mobile{left:775px;top:591px;width:199px;height:2434px}
.menu-panel{left:984px;top:587px;width:197px;height:443px;background:#000;color:#fff}
.abs{position:absolute}
.head{font-family:"Oswald",sans-serif;font-weight:700;text-transform:uppercase;line-height:1.2}
.brand{font-family:"Oswald",sans-serif;font-weight:500;color:var(--leaf-bright);text-transform:uppercase;letter-spacing:.5px;display:flex;align-items:center;gap:5px}
.brand i{display:inline-block;width:10px;height:10px;background:var(--leaf-bright)}
.btn{position:absolute;background:var(--leaf);color:#fff;font-family:"Oswald",sans-serif;font-weight:700;font-size:8px;letter-spacing:1.5px;text-transform:uppercase;display:flex;align-items:center;justify-content:center}
.field{position:absolute;background:#fff;border:1px solid #ccc;font-size:8px;color:#888;display:flex;align-items:center;padding-left:10px}
.link{position:absolute;font-family:"Oswald",sans-serif;font-weight:700;font-size:8px;letter-spacing:1.6px;color:var(--leaf);border-bottom:1px solid var(--leaf);padding-bottom:3px;text-transform:uppercase}
.hero{position:absolute;left:0;top:0;width:100%;background:radial-gradient(ellipse at 55% 35%,#4a3526 0%,#1c130d 45%,#050505 80%)}
.nav{position:absolute;display:flex;gap:28px;font-size:8.5px;color:#fff}
.hero-title{position:absolute;width:100%;text-align:center;color:#fff;font-family:"Oswald",sans-serif;font-weight:700;letter-spacing:4px;text-transform:uppercase}
.hero-text{position:absolute;width:100%;text-align:center;color:#ddd;line-height:1.6}
.faint{position:absolute;font-family:"Oswald",sans-serif;font-weight:700;color:#f0f0f0;letter-spacing:6px;text-transform:uppercase}
p.copy{font-size:7.6px;line-height:1.65;color:#333}
.dark-band{position:absolute;left:0;width:100%;background:radial-gradient(ellipse at 55% 30%,#2f4328 0%,#15200f 55%,#0c130a 100%);color:#fff}
.ticks{position:absolute;list-style:none}
.ticks li{display:flex;gap:10px;font-size:7.4px;line-height:1.5;color:#333;margin-bottom:11px}
.ticks svg{flex:none;margin-top:1px}
.footer{position:absolute;left:0;width:100%;background:var(--dark);color:#fff}
.contact{position:absolute;font-size:7.6px;color:#ccc;line-height:1.5}
.contact div{display:flex;gap:10px;margin-bottom:14px}
.contact b{color:#fff}
.socials{position:absolute;display:flex;gap:10px}
.socials span{width:9px;height:9px;border-radius:50%;background:#fff;display:block}
</style>
</head>
<body>

<div class="stage-band"></div>

<!-- desktop front page -->
<section class="board desktop">
  <div class="hero" style="height:407px" role="img" aria-label="Golfer swinging in a dimly lit simulator room with a projected course screen">
    <div class="brand abs" style="left:100px;top:18px;font-size:20px">Fjordtee Play<i></i></div>
    <nav class="nav" style="left:350px;top:20px"><span>Hjem</span><span>Blog</span><span>Find vej</span><span>Ordbog</span></nav>
    <div class="btn" style="left:554px;top:16px;width:78px;height:20px">Kontakt os</div>
    <h1 class="hero-title" style="top:199px;font-size:27px">Topmoderne teknologi</h1>
    <p class="hero-text" style="top:238px;font-size:8.2px">Vores hightech simulatorer fra SwingTrack fanger med høj præcision bolden fra dit slag.<br>Se alt data på storskærm.</p>
    <div class="btn" style="left:329px;top:281px;width:72px;height:20px">See mere</div>
    <div class="abs" style="left:587px;top:336px;color:#fff;font-family:Oswald,sans-serif;font-weight:700;font-size:22px">1</div>
    <div class="abs" style="left:611px;top:330px;width:1px;height:42px;background:#777"></div>
    <div class="abs" style="left:624px;top:343px;color:#999;font-size:9px">3</div>
  </div>

  <div class="faint" style="left:160px;top:432px;font-size:62px">Fjordtee Play</div>
  <h2 class="head abs" style="left:101px;top:492px;width:240px;font-size:17px">Golfsimulator i Valby åbner januar 2023</h2>
  <div class="abs" style="left:101px;top:553px;width:240px">
    <p class="copy">Til januar 2023 åbner et nyt golfsimulatorcenter i Valby med 8 simulatorer af typen SwingTrack 4. Vi glæder os til at kunne byde velkommen til nye og erfarne golfspillere. Hos os kan du øve alle slags slag indedørs i ly fra regn og sne, eller gå en hel 18-hullers bane på den halve tid.</p>
    <p class="copy" style="margin-top:10px">Hver simulator giver dig en helt præcis radarmåling af dit slag, så du kan øve dig præcis som du vil på en virtuel driving range, eller på en af vores mange virtuelle baner fra hele verdenen.</p>
  </div>
  <svg class="abs" style="left:376px;top:494px" width="342" height="212" role="img" aria-label="Golfer in a blue cap mid-swing against a sky background">
    <defs><linearGradient id="dsky" x1="0" y1="0" x2="1" y2="1"><stop offset="0" stop-color="#5f7e9c"/><stop offset="1" stop-color="#d6dde3"/></linearGradient></defs>
    <polygon points="70,0 268,0 168,212 0,212" fill="url(#dsky)"/>
  </svg>
  <div class="brand abs" style="left:380px;top:654px;font-size:17px">Fjordtee Play<i></i></div>

  <div class="dark-band" style="top:760px;height:309px">
    <h2 class="head abs" style="left:0;top:62px;width:100%;text-align:center;font-size:17px">Åbningsreception</h2>
    <p class="abs" style="left:110px;top:100px;width:508px;text-align:center;font-size:7.6px;line-height:1.6;color:#ddd">Vi holder åbningsreception d. 20. januar 2023 fra klokken 16. Mere information kommer her på siden løbende, og via vores nyhedsbrev, som du kan tilmelde her. Vi giver desuden en rabatkode til 1 times gratis spil til alle, som tilmelder sig vores nyhedsbrev før nytår, og som stadig er tilmeldt nyhedsbrevet til vores åbningsreception.<br><br>Rabatkoden sendes på email senest d. 21. januar, og skal bruges i perioden 1. februar til 31. marts. Der kan kun bruges én rabatkode pr. person. Der uddeles højst 500 rabatkoder. Hvis der er flere tilmeldte, er det efter tidligst tilmelding.</p>
    <div class="field" style="left:225px;top:196px;width:278px;height:28px">Emailadresse</div>
    <div class="btn" style="left:331px;top:240px;width:68px;height:25px">Ja tak!</div>
  </div>

  <div class="abs" style="left:101px;top:1122px;width:150px;height:258px;border-radius:50%;background:radial-gradient(circle at 40% 40%,#fafafa,#9a9a9a)" role="img" aria-label="Close-up of a white golf ball"></div>
  <h2 class="head abs" style="left:270px;top:1184px;width:380px;font-size:29px">Køb et opstartsmedlemsskab allerede nu!</h2>
  <div class="abs" style="left:270px;top:1266px;font-size:13px;color:#222">Til dig selv eller som gave</div>
  <div class="link" style="left:270px;top:1300px">Mere information</div>

  <svg class="abs" style="left:0;top:1426px" width="332" height="196" role="img" aria-label="Golf iron and ball on a green panel">
    <polygon points="48,0 332,0 290,130 0,196 0,80" fill="#2a9a2a"/>
  </svg>
  <h3 class="head abs" style="left:98px;top:1624px;font-size:15px">Opstartsmedlemsskab</h3>
  <ul class="ticks" style="left:98px;top:1658px;width:240px">
    <li><svg width="14" height="12"><path d="M1 7l4 4L13 1" stroke="#1f8a1f" stroke-width="2.2" fill="none"/></svg><span>Lorem ipsum dolor sit amet consectetur.</span></li>
    <li><svg width="14" height="12"><path d="M1 7l4 4L13 1" stroke="#1f8a1f" stroke-width="2.2" fill="none"/></svg><span>Lorem ipsum dolor sit amet consectetur. Lorem <b>ipsum dolor sit amet</b> consectetur.</span></li>
    <li><svg width="14" height="12"><path d="M1 7l4 4L13 1" stroke="#1f8a1f" stroke-width="2.2" fill="none"/></svg><span>Lorem ipsum dolor sit amet consectetur.</span></li>
    <li><svg width="14" height="12"><path d="M1 7l4 4L13 1" stroke="#1f8a1f" stroke-width="2.2" fill="none"/></svg><span>Lorem ipsum dolor sit amet consectetur. Lorem ipsum dolor <b>sit amet consectetur.</b></span></li>
  </ul>
  <div class="link" style="left:98px;top:1779px">Mere information</div>
  <svg class="abs" style="left:376px;top:1469px" width="352" height="348" role="img" aria-label="Woman swinging at a simulator screen showing a green fairway">
    <defs><linearGradient id="dsim" x1="0" y1="0" x2="0" y2="1"><stop offset="0" stop-color="#222"/><stop offset=".5" stop-color="#2c5a2a"/><stop offset="1" stop-color="#173a18"/></linearGradient></defs>
    <polygon points="72,0 352,0 352,348 0,348 30,240" fill="url(#dsim)"/>
  </svg>
  <div class="brand abs" style="left:510px;top:1749px;font-size:19px;color:#fff">Fjordtee Play<i style="background:#fff"></i></div>
  <div class="abs" style="left:460px;top:1780px;font-size:8px;color:#ddd">Opstartsmedlemsskab – tryk for mere information.</div>
  <div class="abs" style="left:320px;top:1523px;width:172px;height:52px;background:var(--teal);color:#fff;text-align:center;transform:rotate(-3deg)">
    <div style="font-family:Montserrat,sans-serif;font-weight:600;font-size:22px;line-height:1.3">KUN 500,-</div>
    <div style="font-size:6px">Normalpris 2000,-</div>
  </div>

  <div class="footer" style="top:1845px;height:236px">
    <div class="contact" style="left:98px;top:50px">
      <div><svg width="8" height="10"><path d="M4 0a4 4 0 0 1 4 4c0 3-4 6-4 6S0 7 0 4a4 4 0 0 1 4-4z" fill="#ccc"/></svg><span>Solbakken 21, 2500 Valby,<br>CVR: 40118652</span></div>
      <div><svg width="8" height="10"><rect x="1" y="0" width="6" height="10" rx="1" fill="none" stroke="#ccc"/></svg><b>40-12-55-80</b></div>
      <div><svg width="9" height="9"><rect x=".5" y="1.5" width="8" height="7" fill="none" stroke="#ccc"/></svg><span><b>15:00 to 22:00</b><br>Monday to Sunday</span></div>
    </div>
    <div class="brand abs" style="left:278px;top:66px;font-size:21px">Fjordtee Play<i></i></div>
    <div class="socials" style="left:305px;top:112px"><span></span><span></span><span></span><span></span><span></span></div>
    <div class="head abs" style="left:479px;top:46px;font-size:8px;letter-spacing:1px">Tilmeld vores nyhedsbrev!</div>
    <div class="field" style="left:479px;top:64px;width:152px;height:27px">Emailadresse</div>
    <div class="btn" style="left:479px;top:102px;width:62px;height:22px">Ja tak!</div>
    <div class="abs" style="left:0;top:210px;width:100%;text-align:center;font-size:6.5px;color:#aaa">©Copyright 2023. FJORDTEE PLAY APS | All Rights Reserved</div>
  </div>
</section>

<!-- mobile front page -->
<section class="board mobile">
  <div class="hero" style="height:440px" role="img" aria-label="Golfer swinging in a dimly lit simulator room">
    <div class="brand abs" style="left:10px;top:21px;font-size:13px">Fjordtee Play<i style="width:7px;height:7px"></i></div>
    <svg class="abs" style="left:174px;top:24px" width="14" height="8"><path d="M0 1h14M0 4h14M0 7h14" stroke="#2aa52a"/></svg>
    <h1 class="hero-title" style="top:297px;font-size:13px;letter-spacing:1.5px">Topmoderne teknolog</h1>
    <p class="hero-text" style="top:320px;left:8px;width:183px;font-size:8px;line-height:1.5">Vores hightech simulatorer fra SwingTrack fanger med høj præcision bolden fra dit slag. Se alt data på storskærm.</p>
    <div class="btn" style="left:61px;top:378px;width:77px;height:20px">See mere</div>
  </div>
  <h2 class="head abs" style="left:8px;top:474px;width:185px;font-size:15px">Golfsimulator i Valby åbner januar 2023</h2>
  <div class="abs" style="left:8px;top:530px;width:185px">
    <p class="copy" style="font-size:7.8px">Til januar 2023 åbner et nyt golfsimulatorcenter i Valby med 8 simulatorer af typen SwingTrack 4. Vi glæder os til at kunne byde velkommen til nye og erfarne golfspillere. Hos os kan du øve alle slags slag indedørs i ly fra regn og sne, eller gå en hel 18-hullers bane på den halve tid.</p>
    <p class="copy" style="font-size:7.8px;margin-top:8px">Hver simulator giver dig en helt præcis radarmåling af dit slag, så du kan øve dig præcis som du vil på en virtuel driving range, eller på en af vores mange virtuelle baner fra hele verdenen.</p>
  </div>
  <div class="faint" style="left:8px;top:719px;font-size:28px;letter-spacing:2px">Fjordtee Play</div>
  <svg class="abs" style="left:8px;top:749px" width="190" height="146" role="img" aria-label="Golfer in a blue cap mid-swing against a sky">
    <defs><linearGradient id="msky" x1="0" y1="0" x2="1" y2="1"><stop offset="0" stop-color="#5f7e9c"/><stop offset="1" stop-color="#d6dde3"/></linearGradient></defs>
    <polygon points="40,0 186,0 110,146 0,146" fill="url(#msky)"/>
  </svg>
  <div class="brand abs" style="left:10px;top:872px;font-size:11px">Fjordtee Play<i style="width:7px;height:7px"></i></div>

  <div class="dark-band" style="top:928px;height:394px">
    <h2 class="head abs" style="left:0;top:38px;width:100%;text-align:center;font-size:14px">Åbningsreception</h2>
    <p class="abs" style="left:10px;top:64px;width:179px;text-align:center;font-size:7.7px;line-height:1.6;color:#ddd">Vi holder åbningsreception d. 20. januar 2023 fra klokken 16. Mere information kommer her på siden løbende, og via vores nyhedsbrev, som du kan tilmelde her. Vi giver desuden en rabatkode til 1 times gratis spil til alle, som tilmelder sig vores nyhedsbrev før nytår, og som stadig er tilmeldt nyhedsbrevet til vores åbningsreception.<br><br>Rabatkoden sendes på email senest d. 21. januar, og skal bruges i perioden 1. februar til 31. marts. Der kan kun bruges én rabatkode pr. person. Der uddeles højst 500 rabatkoder. Hvis der er flere tilmeldte, er det efter tidligst tilmelding.</p>
    <div class="field" style="left:8px;top:294px;width:184px;height:28px">Emailadresse</div>
    <div class="btn" style="left:65px;top:341px;width:70px;height:22px">Ja tak!</div>
  </div>

  <div class="abs" style="left:-30px;top:1330px;width:70px;height:185px;border-radius:50%;background:radial-gradient(circle at 60% 40%,#fafafa,#a5a5a5)" role="img" aria-label="White golf ball"></div>
  <h2 class="head abs" style="left:14px;top:1362px;width:180px;text-align:center;font-size:15px">Køb et opstartsmedlemsskab allerede nu!</h2>
  <div class="abs" style="left:0;top:1432px;width:100%;text-align:center;font-size:10.5px">Til dig selv eller som gave</div>
  <div class="link" style="left:50px;top:1456px">Mere information</div>

  <svg class="abs" style="left:0;top:1541px" width="199" height="144" role="img" aria-label="Simulator screen with a fairway and a woman swinging">
    <defs><linearGradient id="msim" x1="0" y1="0" x2="0" y2="1"><stop offset="0" stop-color="#222"/><stop offset=".5" stop-color="#2c5a2a"/><stop offset="1" stop-color="#173a18"/></linearGradient></defs>
    <polygon points="75,0 199,0 199,144 40,144 50,80" fill="url(#msim)"/>
  </svg>
  <div class="abs" style="left:6px;top:1600px;width:90px;height:32px;background:var(--teal);color:#fff;text-align:center;transform:rotate(-3deg)">
    <div style="font-weight:600;font-size:14px;line-height:1.4">KUN 500,-</div>
    <div style="font-size:4.5px">Normalpris 2000,-</div>
  </div>
  <div class="brand abs" style="left:88px;top:1651px;font-size:10px;color:#fff">Fjordtee Play<i style="width:6px;height:6px;background:#fff"></i></div>
  <div class="abs" style="left:60px;top:1672px;font-size:4.8px;color:#ddd">Opstartsmedlemsskab – tryk for more information.</div>

  <h3 class="head abs" style="left:8px;top:1704px;font-size:14px">Opstartsmedlemsskab</h3>
  <ul class="ticks" style="left:6px;top:1740px;width:186px">
    <li style="font-size:7px;margin-bottom:9px"><svg width="12" height="10"><path d="M1 6l3 3L11 1" stroke="#1f8a1f" stroke-width="2" fill="none"/></svg><span>Lorem ipsum dolor sit amet consectetur.</span></li>
    <li style="font-size:7px;margin-bottom:9px"><svg width="12" height="10"><path d="M1 6l3 3L11 1" stroke="#1f8a1f" stroke-width="2" fill="none"/></svg><span>Lorem ipsum dolor sit amet consectetur. Lorem <b>ipsum dolor sit amet</b> consectetur.</span></li>
    <li style="font-size:7px;margin-bottom:9px"><svg width="12" height="10"><path d="M1 6l3 3L11 1" stroke="#1f8a1f" stroke-width="2" fill="none"/></svg><span>Lorem ipsum dolor sit amet consectetur.</span></li>
    <li style="font-size:7px;margin-bottom:9px"><svg width="12" height="10"><path d="M1 6l3 3L11 1" stroke="#1f8a1f" stroke-width="2" fill="none"/></svg><span>Lorem ipsum dolor sit amet consectetur. Lorem ipsum dolor <b>sit amet consectetur.</b></span></li>
  </ul>
  <div class="link" style="left:8px;top:1866px">Mere information</div>
  <svg class="abs" style="left:0;top:1901px" width="199" height="119" role="img" aria-label="Golf iron and ball on a green panel">
    <polygon points="30,0 199,0 170,75 0,119 0,50" fill="#2a9a2a"/>
  </svg>

  <div class="footer" style="top:2050px;height:384px">
    <div class="brand abs" style="left:0;top:40px;width:100%;justify-content:center;font-size:24px">Fjordtee Play<i style="width:12px;height:12px"></i></div>
    <div class="socials" style="left:53px;top:84px"><span></span><span></span><span></span><span></span><span></span></div>
    <div class="head abs" style="left:0;top:125px;width:100%;text-align:center;font-size:8px;letter-spacing:1px">Tilmeld vores nyhedsbrev!</div>
    <div class="field" style="left:8px;top:145px;width:184px;height:28px">Emailadresse</div>
    <div class="btn" style="left:69px;top:192px;width:62px;height:22px">Ja tak!</div>
    <div class="contact" style="left:40px;top:243px;font-size:7.6px">
      <div><svg width="8" height="10"><path d="M4 0a4 4 0 0 1 4 4c0 3-4 6-4 6S0 7 0 4a4 4 0 0 1 4-4z" fill="#ccc"/></svg><span>Solbakken 21, 2500 Valby,<br>CVR: 40118652</span></div>
      <div><svg width="8" height="10"><rect x="1" y="0" width="6" height="10" rx="1" fill="none" stroke="#ccc"/></svg><b>40-12-55-80</b></div>
      <div><svg width="9" height="9"><rect x=".5" y="1.5" width="8" height="7" fill="none" stroke="#ccc"/></svg><span><b>15:00 to 22:00</b><br>Monday to Sunday</span></div>
    </div>
    <div class="abs" style="left:0;top:363px;width:100%;text-align:center;font-size:4.8px;color:#aaa">©Copyright 2023. FJORDTEE PLAY APS | All Rights Reserved</div>
  </div>
</section>

<!-- mobile menu open -->
<section class="board menu-panel" role="img" aria-label="Mobile navigation over a darkened golfer photo" style="background:radial-gradient(ellipse at 40% 20%,#3a2a20 0%,#0a0705 60%,#000 100%)">
  <div class="brand abs" style="left:15px;top:22px;font-size:13px">Fjordtee Play<i style="width:7px;height:7px"></i></div>
  <svg class="abs" style="left:175px;top:22px" width="12" height="12"><path d="M1 1l10 10M11 1L1 11" stroke="#2aa52a" stroke-width="1.4"/></svg>
  <nav class="abs" style="left:0;top:92px;width:100%;text-align:center;font-size:8.5px;line-height:34px">Hjem<br>Blog<br>Find vej<br>Ordbog</nav>
  <div class="btn" style="left:60px;top:238px;width:78px;height:21px">Kontakt os</div>
  <div class="socials" style="left:50px;top:300px"><span></span><span></span><span></span><span></span><span></span></div>
  <div class="contact" style="left:38px;top:339px;font-size:7.6px">
    <div><svg width="8" height="10"><path d="M4 0a4 4 0 0 1 4 4c0 3-4 6-4 6S0 7 0 4a4 4 0 0 1 4-4z" fill="#ccc"/></svg><span>Solbakken 21, 2500 Valby,<br>CVR: 40118652</span></div>
    <div><svg width="8" height="10"><rect x="1" y="0" width="6" height="10" rx="1" fill="none" stroke="#ccc"/></svg><b>40-12-55-80</b></div>
    <div><svg width="9" height="9"><rect x=".5" y="1.5" width="8" height="7" fill="none" stroke="#ccc"/></svg><span><b>15:00 to 22:00</b><br>Monday to Sunday</span></div>
  </div>
</section>

</body>
</html>
```